Wealth management firm needs a business card design

Using my logo, create a business card that covers all of the regulatory wordings that I need. It must have - Registered Office 5-7 Pellinore Court, Edinburgh, EH9 2QW. Registered in Scotland under number SC738204. Corvell Wealth Management Ltd is an appointed representative of Quintor wealth management Ltd, which is authorised and regulated by the Monetary Standards Council.

Target Market(s)

professional clients

Industry/Entity Type

finance

Contact Information for Business Card

Corvell Wealth Management, Rupert Ashdown-Kerr, Director, 9 Tanner Row, Edinburgh, EH2 4NP. 07812 455 193, rupert.ashdown-kerr@corvellwealth.example , www.corvellwealth.example

Font styles to use
Serif

Colors
0054AA
0677BA
7BADD7
CADEEF
E8F1F8

Requirements
Must have
• regulatory wording in small text at bottom

```html
<!DOCTYPE html>
<html lang="en">
<head>
<meta charset="utf-8">
<title>Corvell Wealth Management – Business Card</title>
<link rel="stylesheet" href="https://fonts.googleapis.com/css2?family=Noto+Serif:wght@400;700&display=swap">
<style>
  :root {
    --page-bg: #d6d6d6;
    --card-white: #ffffff;
    --brand-blue: #2f6fb7;
    --ink: #2a2a2a;
    --on-blue: #ffffff;
    --on-blue-soft: #e8f1f8;
    --divider: #6d9bd3;
  }
  * { box-sizing: border-box; margin: 0; padding: 0; }
  html, body {
    width: 1200px; height: 802px; overflow: hidden;
    background: var(--page-bg);
    font-family: "Noto Serif", Georgia, serif;
  }
  .sheet {
    width: 1200px; height: 802px;
    display: flex; align-items: center; justify-content: center; gap: 40px;
  }
  .card {
    width: 540px; height: 309px; border-radius: 22px;
    position: relative; overflow: hidden; flex: none;
    box-shadow: 0 6px 18px rgba(0,0,0,0.18);
  }

  /* Front */
  .card--front { background: var(--card-white); display: flex; align-items: center; padding-right: 20px; }
  .brand-block {
    width: 210px; flex: none; display: flex; flex-direction: column; align-items: center; gap: 3px;
    padding-left: 12px;
  }
  .brand-mark { width: 30px; height: 30px; border-radius: 50%; background: var(--brand-blue); margin-bottom: 6px; }
  .brand-name { font-size: 13px; font-weight: 400; color: var(--ink); white-space: nowrap; }
  .brand-tagline { font-size: 7px; color: var(--ink); letter-spacing: 0.2px; }
  .divider { width: 1px; height: 160px; flex: none; background: var(--divider); margin: 0 14px 0 12px; }
  .contact { display: flex; flex-direction: column; color: var(--ink); min-width: 0; }
  .contact__name { font-size: 20px; font-weight: 700; color: var(--brand-blue); line-height: 1.15; white-space: nowrap; }
  .contact__role, .contact__line { font-size: 12px; line-height: 1.42; }
  .contact__role { margin-bottom: 6px; }
  .contact__address { margin-bottom: 4px; }
  .contact__item { display: flex; align-items: center; gap: 6px; font-size: 11px; line-height: 1.6; white-space: nowrap; }
  .contact__item svg { width: 11px; height: 11px; fill: var(--brand-blue); flex: none; }

  /* Back */
  .card--back {
    background: var(--brand-blue); color: var(--on-blue);
    display: flex; flex-direction: column; align-items: center; text-align: center;
    padding: 32px 36px 0;
  }
  .back-mark { width: 58px; height: 58px; border-radius: 50%; background: var(--on-blue); margin-bottom: 14px; }
  .back-name { font-size: 25px; font-weight: 400; line-height: 1.1; white-space: nowrap; }
  .back-tagline { font-size: 10px; margin-top: 4px; letter-spacing: 0.4px; }
  .registration { margin-top: 22px; font-size: 11px; line-height: 1.55; }
  .regulatory {
    position: absolute; left: 36px; right: 36px; bottom: 16px;
    font-size: 8px; line-height: 1.45; color: var(--on-blue-soft);
  }
</style>
</head>
<body>
<main class="sheet">
  <section class="card card--front" aria-label="Business card front">
    <div class="brand-block">
      <span class="brand-mark" aria-hidden="true"></span>
      <span class="brand-name">Corvell Wealth Management Ltd</span>
      <span class="brand-tagline">Personal Financial Advice</span>
    </div>
    <div class="divider" aria-hidden="true"></div>
    <div class="contact">
      <span class="contact__name">Rupert Ashdown-Kerr</span>
      <span class="contact__role">Director</span>
      <div class="contact__address">
        <div class="contact__line">9 Tanner Row</div>
        <div class="contact__line">Edinburgh, EH2 4NP</div>
      </div>
      <div class="contact__item">
        <svg viewBox="0 0 24 24" aria-hidden="true"><path d="M6.6 10.8a15.1 15.1 0 0 0 6.6 6.6l2.2-2.2c.3-.3.7-.4 1-.2 1.1.4 2.3.6 3.6.6.6 0 1 .4 1 1V20c0 .6-.4 1-1 1A17 17 0 0 1 3 4c0-.6.4-1 1-1h3.5c.6 0 1 .4 1 1 0 1.3.2 2.5.6 3.6.1.3 0 .7-.2 1z"/></svg>
        07812 455 193
      </div>
      <div class="contact__item">
        <svg viewBox="0 0 24 24" aria-hidden="true"><path d="M2 5h20v14H2zm2 2v.5l8 5 8-5V7z"/></svg>
        rupert.ashdown-kerr@corvellwealth.example
      </div>
      <div class="contact__item">
        <svg viewBox="0 0 24 24" aria-hidden="true"><path d="M12 2a10 10 0 1 0 0 20 10 10 0 0 0 0-20zm6.9 9h-3a15 15 0 0 0-1.3-5.6A8 8 0 0 1 18.9 11zM12 4c1 1.3 1.8 3.9 1.9 7h-3.8C10.2 7.9 11 5.3 12 4zM9.4 5.4A15 15 0 0 0 8.1 11h-3a8 8 0 0 1 4.3-5.6zM5.1 13h3a15 15 0 0 0 1.3 5.6A8 8 0 0 1 5.1 13zM12 20c-1-1.3-1.8-3.9-1.9-7h3.8c-.1 3.1-.9 5.7-1.9 7zm2.6-1.4a15 15 0 0 0 1.3-5.6h3a8 8 0 0 1-4.3 5.6z"/></svg>
        www.corvellwealth.example
      </div>
    </div>
  </section>

  <section class="card card--back" aria-label="Business card back">
    <span class="back-mark" aria-hidden="true"></span>
    <span class="back-name">Corvell Wealth Management Ltd</span>
    <span class="back-tagline">Personal Financial Advice</span>
    <p class="registration">
      Registered Office 5-7 Pellinore Court, Edinburgh, EH9 2QW<br>
      Registered in Scotland under number SC738204
    </p>
    <p class="regulatory">
      Corvell Wealth Management Ltd is an appointed representative of Quintor wealth management Ltd,
      which is authorised and regulated by the Monetary Standards Council.
    </p>
  </section>
</main>
</body>
</html>
```